We are needing a bookcover for a reprint of our book "Whispers Beneath the Amber Horizon". It takes a look at the geologic formation found in the great plains. Our original cover was colorful and showed rock layers. Something similar but different and eye catching would be great. a geologic cross section showing various layers or possibly some different rocks/soils. We are really open to suggestions attached is the current book cover with the colored layers and the cover from the 80s.

Target Market(s)

Adult Readers

Industry/Entity Type

Nonprofit retail - science - nature

Requirements
Must have
• Geology or rock layers
Nice to have
• Books title, Geologic cross section
Should not have
• People or animals, no photos prefer sketch

```html
<!DOCTYPE html>
<html lang="en">
<head>
<meta charset="utf-8">
<title>Whispers Beneath the Amber Horizon — Book Cover</title>
<link rel="stylesheet" href="https://fonts.googleapis.com/css2?family=Bebas+Neue&display=swap">
<style>
  :root {
    --page-bg: #e8e8e8;
    --title-box: #361c06;
    --title-ink: #f8f2c8;
    --strata-dark: #4a3328;
    --strata-rust: #9a4a2e;
    --strata-amber: #d98a3c;
    --strata-sand: #d8c3a0;
    --strata-teal: #3f7a74;
  }
  html, body {
    margin: 0;
    width: 1200px;
    height: 1200px;
    overflow: hidden;
    background: var(--page-bg);
  }
  .book-cover {
    position: absolute;
    left: 278px;
    top: 110px;
    width: 644px;
    height: 981px;
    overflow: hidden;
    box-shadow: 0 4px 18px rgba(0,0,0,0.18);
  }
  .strata-art {
    position: absolute;
    inset: 0;
    width: 100%;
    height: 100%;
    display: block;
  }
  .title-box {
    position: absolute;
    left: 164px;
    top: 93px;
    width: 316px;
    height: 312px;
    background: var(--title-box);
    display: flex;
    flex-direction: column;
    align-items: center;
    justify-content: center;
  }
  .title-box p {
    margin: 0;
    font-family: "Bebas Neue", sans-serif;
    font-size: 72px;
    line-height: 74px;
    color: var(--title-ink);
    text-align: center;
  }
  .title-main {
    position: absolute;
    left: 0;
    right: 0;
    top: 470px;
    margin: 0;
    font-family: "Bebas Neue", sans-serif;
    font-weight: 400;
    font-size: 176px;
    line-height: 158px;
    color: var(--title-ink);
    text-align: center;
  }
</style>
</head>
<body>
  <main class="book-cover">
    <svg class="strata-art" viewBox="0 0 644 981" preserveAspectRatio="none" role="img" aria-label="Sketched geologic cross section of folded rock layers in brown, rust, amber, cream and teal">
      <defs>
        <linearGradient id="strataLeft" x1="0" y1="0" x2="0" y2="1">
          <stop offset="0" stop-color="var(--strata-dark)"/>
          <stop offset="0.25" stop-color="var(--strata-rust)"/>
          <stop offset="0.45" stop-color="#6b5a52"/>
          <stop offset="0.6" stop-color="var(--strata-rust)"/>
          <stop offset="0.78" stop-color="#8a6a55"/>
          <stop offset="0.9" stop-color="var(--strata-teal)"/>
          <stop offset="1" stop-color="var(--strata-dark)"/>
        </linearGradient>
        <linearGradient id="strataRight" x1="0" y1="0" x2="0" y2="1">
          <stop offset="0" stop-color="#a89a88"/>
          <stop offset="0.2" stop-color="var(--strata-amber)"/>
          <stop offset="0.42" stop-color="var(--strata-sand)"/>
          <stop offset="0.62" stop-color="#c8705a"/>
          <stop offset="0.8" stop-color="var(--strata-amber)"/>
          <stop offset="0.92" stop-color="var(--strata-teal)"/>
          <stop offset="1" stop-color="#c9a07a"/>
        </linearGradient>
      </defs>
      <rect x="0" y="0" width="330" height="981" fill="url(#strataLeft)"/>
      <rect x="330" y="0" width="314" height="981" fill="url(#strataRight)"/>
    </svg>

    <div class="title-box">
      <p>Whispers</p>
      <p>Beneath</p>
      <p>the</p>
    </div>

    <h1 class="title-main">Amber<br>Horizon</h1>
  </main>
</body>
</html>
```